Tabloid Magazine Flyer Class Action Lawsuit

Create a bold, 2-page 8.5" x 11" flyer with the look and feel of a tabloid exposé — loud, sensational, and impossible to ignore. Use bold fonts, dramatic headlines, and high-contrast colors (red, black, white, deep blue). Fill every inch of space — no white space, no subtlety. Use the provided images prominently. Page 1 should grab attention with a shocking headline, impactful image, and strong call to action. Page 2 should stack bold subheadings and explosive bullet points. Emphasize urgency, outrage, and grassroots power. This flyer is meant to rally a community.
Updates

Need to extend because we haven't received a design that meets our needs

Target Market(s)

All instructions and content are in the attached word doc

Industry/Entity Type

Requirements
Must have
• All instructions and content are in the attached word doc
Nice to have
Should not have

```html
<!DOCTYPE html>
<html lang="en">
<head>
<meta charset="utf-8">
<title>Seacrest Park Community Flyer</title>
<link rel="stylesheet" href="https://fonts.googleapis.com/css2?family=Oswald:wght@700&family=Poppins:wght@500;600;700;800&display=swap">
<style>
:root{
  --bg:#b4b4b4;
  --paper:#ffffff;
  --yellow:#fff200;
  --red:#d21f26;
  --black:#0b0b0b;
  --navy:#22377a;
  --white:#ffffff;
}
*{box-sizing:border-box;margin:0;padding:0}
html,body{width:1200px;height:1117px;overflow:hidden;background:var(--bg)}
.headline{font-family:"Oswald",Impact,sans-serif;font-weight:700;text-transform:uppercase;line-height:1}
.page{position:absolute;top:239px;width:540px;height:702px;background:var(--paper);padding:8px}
.page--front{left:51px}
.page--back{left:616px}
.sheet{position:relative;width:524px;height:686px;overflow:hidden;background:var(--navy)}
.abs{position:absolute}
.ph{position:absolute}

/* front */
.expose-box{left:0;top:0;width:344px;height:126px;background:var(--yellow);color:var(--black);display:flex;align-items:center;justify-content:center;text-align:center;font-size:26px;line-height:1;padding-top:2px}
.fight-box{left:344px;top:0;width:180px;height:186px;background:var(--red);text-align:center;padding-top:10px;font-size:30px;line-height:0.9;color:var(--white)}
.fight-box .hl{color:var(--yellow)}
.public-band{left:0;top:126px;width:344px;height:60px;background:var(--black);color:var(--white);font:700 12.4px/1.15 "Poppins",Arial,sans-serif;text-align:center;text-transform:uppercase;display:flex;align-items:center;justify-content:center}
.hero{left:0;top:186px;width:524px;height:206px;background:linear-gradient(90deg,#233a85 0%,#2a4190 44%,#6a6f9a 52%,#9b7d8e 70%,#c25a5f 100%)}
.stop-photo{left:361px;top:130px;width:144px;height:143px;background:radial-gradient(circle,#ffffff 0%,#e8b3b5 45%,#d21f26 100%)}
.hero-copy{left:17px;top:194px;color:var(--yellow)}
.hero-copy .l1{font-size:30px;line-height:0.94}
.hero-copy .l2{font-size:24px;color:var(--white);line-height:0.93;margin-top:2px}
.hero-copy .l3{font-size:46px;line-height:1.05}
.restrooms{left:0;top:392px;width:220px;height:144px;background:linear-gradient(180deg,#9fb8d6 0%,#c9d3de 45%,#3f87c4 70%,#5c6a78 100%)}
.meeting{left:220px;top:392px;width:304px;height:144px;text-align:center;color:var(--white)}
.meeting .join{font:700 12.5px/1 "Poppins",Arial,sans-serif;margin-top:16px}
.meeting .name{font:700 23px/1 "Poppins",Arial,sans-serif;margin-top:4px}
.meeting .date{display:inline-block;background:var(--yellow);color:var(--black);font:700 15px/1 "Poppins",Arial,sans-serif;padding:5px 8px;margin-top:6px}
.meeting .place{font:700 11.4px/1.2 "Poppins",Arial,sans-serif;margin-top:7px}
.meeting .place b{color:var(--yellow)}
.lawsuit{left:0;top:536px;width:524px;height:91px}
.lawsuit .title{position:absolute;left:39px;top:13px;width:445px;height:25px;background:var(--red);color:var(--white);font:700 19.5px/25px "Poppins",Arial,sans-serif;text-align:center}
.lawsuit .detail{position:absolute;left:24px;top:38px;width:475px;height:27px;background:var(--red);color:var(--white);font:700 10px/13px "Poppins",Arial,sans-serif;text-align:center;padding-top:1px}
.lawsuit .urgent{position:absolute;left:92px;top:65px;width:338px;height:14px;background:var(--red);color:var(--yellow);font:700 10px/14px "Poppins",Arial,sans-serif;text-align:center}
.footer{left:0;top:627px;width:524px;height:59px;background:var(--black);color:var(--white);font:700 26px/59px "Poppins",Arial,sans-serif;padding-left:18px}
.partner{left:384px;top:627px;width:140px;height:59px;background:var(--white);display:flex;align-items:center;justify-content:center;text-align:center;font:800 13px/1.15 "Poppins",Arial,sans-serif;color:var(--black);text-transform:uppercase}

/* back */
.expose-lead{left:0;top:0;width:320px;height:116px;background:var(--red);color:var(--white);font:700 10.4px/12.2px "Poppins",Arial,sans-serif;padding:18px 10px 0 28px}
.expose-lead .hl{color:var(--yellow)}
.court-photo{left:320px;top:0;width:204px;height:116px;background:linear-gradient(120deg,#8a5a33 0%,#3b64a8 35%,#2f4f8c 55%,#6b3a26 80%,#3a1c12 100%)}
.split{left:0;top:116px;width:524px;height:5px;background:var(--white)}
.know-band{left:0;top:121px;width:524px;height:41px;background:var(--yellow);color:var(--black);font:800 22.5px/41px "Poppins",Arial,sans-serif;text-align:center}
.facts{top:175px;width:234px}
.facts--left{left:27px}
.facts--right{left:271px}
.fact{margin-bottom:11px}
.fact h3{font:700 10.6px/12.6px "Poppins",Arial,sans-serif;color:var(--yellow);text-transform:uppercase}
.fact p{font:500 9.2px/10.4px "Poppins",Arial,sans-serif;color:var(--white);margin-top:1px}
.fact strong{font-weight:800}
.park-photo{left:246px;top:530px;width:278px;height:97px;background:linear-gradient(180deg,#1b2f5e 0%,#5a4b5c 40%,#b3874e 65%,#6e6e74 100%)}
.tag{position:absolute;background:var(--red);font-family:"Oswald",Impact,sans-serif;font-weight:700;text-transform:uppercase;line-height:1;padding:1px 5px}
.tag--yellow{color:var(--yellow)}
.tag--white{color:var(--white)}
.footer--back{text-align:center;padding-left:0;font-size:33px}
</style>
</head>
<body>

<section class="page page--front">
  <div class="sheet">
    <div class="abs expose-box headline">Seacrest Park Exposed<br>Disabled Child<br>Traumatized Public Land<br>Abused for Profit</div>
    <div class="abs fight-box headline">Help Our<br>Beach<br><span class="hl">Community<br>Fight Back</span></div>
    <div class="abs public-band">Seacrest Park is not private.<br>It is public property owned by the city,<br>paid for by you.</div>
    <div class="ph hero" role="img" aria-label="Photo of a performer on stage facing a large crowd at a beach concert"></div>
    <div class="ph stop-photo" role="img" aria-label="Photo of a stop sign reading No Public Access"></div>
    <div class="abs hero-copy headline">
      <div class="l1">Help Our<br>Community Save<br>Seacrest Park</div>
      <div class="l2">Seacrest Park was<br>built for families —</div>
      <div class="l3">NoTraves</div>
    </div>
    <div class="ph restrooms" role="img" aria-label="Photo of a row of portable toilets lined up beside the park arcade and roller coaster"></div>
    <div class="abs meeting">
      <div class="join">JOIN US &amp; SHOW YOUR SUPPORT @</div>
      <div class="name">CORAL BEACH TOWN<br>COUNCIL MEETING</div>
      <div class="date">DATE: MAY 14, 2025 – 6:00 PM</div>
      <div class="place"><b>PLACE:</b> SEACREST PARK COMMUNITY ROOM<br>(ABOVE THE ARCADE)</div>
    </div>
    <div class="abs lawsuit">
      <div class="title">CLASS ACTION LAWSUIT FORMING NOW!</div>
      <div class="detail">IF YOU'VE BEEN IMPACTED BY NOISE, DENIED PUBLIC ACCESS, OR HARMED BY THESE<br>VIOLATIONS, YOU MAY BE ELIGIBLE FOR COMPENSATION.</div>
      <div class="urgent">WE'RE GATHERING STORIES AND PREPARING LEGAL ACTION.</div>
    </div>
    <div class="abs footer">www.FixSeacrestPark.com</div>
    <div class="abs partner">Access Equals<br>Rights</div>
  </div>
</section>

<section class="page page--back">
  <div class="sheet">
    <div class="abs expose-lead"><span class="hl">XPOSED: Marco Venturi,</span> CEO of Meridian Asset Pool XII LLC the leaseholder of Seacrest Park, has drawn community outrage for profiting off public land while operating Seacrest Park in ways many say violate its lease and damage our beach, our peace, and our environment — all from his luxury estate in Oak Hollow.</div>
    <div class="ph court-photo" role="img" aria-label="Photo of a class action law book with scales of justice beside a judge's gavel"></div>
    <div class="abs split"></div>
    <div class="abs know-band">WHAT THEY DON'T WANT YOU TO KNOW:</div>

    <div class="abs facts facts--left">
      <div class="fact"><h3>Illegal Raves – No Permits.</h3><p>Explosive concerts over 100 decibels, blasting Coral Beach with bass — multiple times per week. According to Public Records these events had <strong>NO PERMITS &amp; NO CITY APPROVAL.</strong></p></div>
      <div class="fact"><h3>The Beach House isn't<br>theirs – it's yours.</h3><p>Seacrest Park is shutting down public space for 9 private Beach House raves through July. But July 5 is different — “Liberty Bash” is a full-park, alcohol-fueled rave that shuts out the public from taxpayer-owned land. These takeovers appear to violate their lease and Prop G, which protects YOUR beach for ALL — not just paying partiers.</p></div>
      <div class="fact"><h3>Disabled child traumatized<br>by rave noise</h3><p>A child with cerebral palsy and auditory sensitivity came to use the City's Beach Accessibility Program but was overwhelmed by deafening Rave noise and fled in distress. The illegal sound levels deny All individuals with similar disabilities access to public accommodations. This is a direct violation of the Americans with Disabilities Act.</p></div>
    </div>

    <div class="abs facts facts--right">
      <div class="fact"><h3>Exposed: Is Seacrest running an unethical self-dealing scheme ?</h3><p>Seacrest Park's General Manager, Grant Holloway, is also CEO of KL Guard Services — the very company hired by Seacrest for “security” services. And who's listed as corporate secretary? Carla Venturi, close relative of the leaseholder Marco Venturi. Is this Self-Dealing?</p></div>
      <div class="fact"><h3>Documented runoff and suspected environmental disaster</h3><p>Improperly Stored Chemicals, oils, and waste water spilling into storm drains. Parking lots are trashed, flooded, and neglected. Stormwater compliance appears to be ignored.</p></div>
      <div class="fact"><h3>Exposed: Seacrest Park's illegal signs mislead the public.</h3><p>They're tricking the public into believing city-owned land is private, violating their lease which requires signage clearly stating the property is city-owned and open to all.</p></div>
      <div class="fact"><h3>Seacrest Park: Accident waiting to happen?</h3><p>From the Big Comet to the rides and walkways, safety appears ignored. The lease requires independent engineer inspections — yet no reports can be found. With what looks like hundreds of code violations, the entire park may be one broken bolt from disaster. Who's protecting the public?</p></div>
    </div>

    <div class="ph park-photo" role="img" aria-label="Aerial evening photo of the amusement park with its wooden roller coaster and parking lot"></div>
    <div class="tag tag--yellow" style="left:13px;top:495px;font-size:23px">Help Our Community</div>
    <div class="tag tag--yellow" style="left:19px;top:519px;font-size:23px">Save Seacrest Park</div>
    <div class="tag tag--white" style="left:13px;top:543px;font-size:19px">Seacrest Park was built</div>
    <div class="tag tag--white" style="left:54px;top:565px;font-size:19px">For Families —</div>
    <div class="tag tag--white" style="left:27px;top:586px;font-size:44px;line-height:0.95;padding:0 6px">NoTraves</div>

    <div class="abs footer footer--back">www.FixSeacrestPark.com</div>
  </div>
</section>

</body>
</html>
```